Real estate agent needs a fresh look for bus bench sign and business card

My wife needs a new and fresh look for her business cards and bus bench advertising. The existing sign is "ok" but it is just that -"ok".

The overall product should communicate trust, confidence and professionalism. Both card and sign should be consistent. The proposed sign must include her face, her phone number 306.847.3160, a VELORA logo with a Marla Quenby Realty line (red +blue preferred), as she is part of a larger group of realtors.. A tagline is optional.

Most agents use a headshot and I personally do not know if this is 100% necessary but if the artwork looks more professional than that is a consideration.

Most of the information on the business card should be included except the QR code.
Updates

Hello,

Sorry but I had a question regarding the logo colour.  The official Velora colours are red and navy blue although we broke the rules and just used the background colours. Red and blue is preferred.  Thanks

Reason: We are looking for a clean minimalistic look with consistent use of fonts. For those that have submitted designs with "fog" fade transitions or a "busy" look please feel free to resubmit. The end product should be crisp, easy on the eyes without any faded transitions. Thank you

Industry/Entity Type

Business

Requirements
Must have
• head shot, 306.847.3160, Marla Quenby Realty, Velora logo, bench size is 20"x 71" + 1" bleed

```html
<!DOCTYPE html>
<html lang="en">
<head>
<meta charset="utf-8">
<title>Dana Whitlock – Bench Sign</title>
<link rel="stylesheet" href="https://fonts.googleapis.com/css2?family=Federant&family=Open+Sans:ital,wght@0,700;0,800;1,600&display=swap">
<style>
  :root {
    --band-light: #eef2f8;
    --band-navy: #1c2d57;
    --accent-red: #d3202f;
    --ink-navy: #1c2d57;
    --paper: #ffffff;
    --photo-tone: #8f7466;
  }
  html, body {
    margin: 0;
    padding: 0;
    width: 1200px;
    height: 362px;
    overflow: hidden;
    background: var(--paper);
  }
  .bench-sign {
    position: relative;
    width: 1200px;
    height: 362px;
    box-sizing: border-box;
    border: 6px solid var(--paper);
    background: var(--band-navy);
    overflow: hidden;
  }
  .top-band {
    position: absolute;
    left: 0; top: 0;
    width: 100%;
    height: 112px;
    background: var(--band-light);
  }
  .accent-rule {
    position: absolute;
    left: 0; top: 112px;
    width: 100%;
    height: 5px;
    background: var(--accent-red);
  }
  .agent-name,
  .agent-phone {
    position: absolute;
    right: 314px;
    margin: 0;
    font-family: "Federant", serif;
    font-weight: 400;
    line-height: 1;
    white-space: nowrap;
  }
  .agent-name {
    top: 26px;
    font-size: 74px;
    letter-spacing: 1px;
    color: var(--ink-navy);
  }
  .agent-phone {
    top: 118px;
    font-size: 84px;
    letter-spacing: 3px;
    color: var(--paper);
  }
  .brokerage {
    position: absolute;
    left: 46px;
    top: 238px;
    color: var(--paper);
    font-family: "Open Sans", sans-serif;
  }
  .brokerage-mark {
    display: flex;
    align-items: center;
    gap: 10px;
  }
  .brokerage-square {
    width: 30px;
    height: 30px;
    background: var(--accent-red);
  }
  .brokerage-name {
    font-weight: 800;
    font-size: 44px;
    line-height: 1;
    letter-spacing: -1px;
  }
  .brokerage-office {
    display: block;
    margin-top: 8px;
    font-weight: 700;
    font-size: 17px;
  }
  .tagline {
    position: absolute;
    right: 314px;
    top: 290px;
    margin: 0;
    font-family: "Open Sans", sans-serif;
    font-style: italic;
    font-weight: 600;
    font-size: 27px;
    line-height: 1.1;
    color: var(--paper);
    white-space: nowrap;
  }
  .headshot {
    position: absolute;
    left: 902px;
    top: 22px;
    width: 236px;
    height: 306px;
    box-sizing: border-box;
    border: 4px solid var(--paper);
    background: var(--photo-tone);
  }
</style>
</head>
<body>
  <main class="bench-sign">
    <div class="top-band"></div>
    <div class="accent-rule"></div>
    <h1 class="agent-name">Dana Whitlock</h1>
    <p class="agent-phone">847-3160</p>
    <div class="brokerage">
      <div class="brokerage-mark">
        <span class="brokerage-square"></span>
        <span class="brokerage-name">VELORA</span>
      </div>
      <span class="brokerage-office">Marla Quenby Realty</span>
    </div>
    <p class="tagline">Serving your regina real estate needs</p>
    <div class="headshot" role="img" aria-label="Headshot portrait of the agent"></div>
  </main>
</body>
</html>
```